Real Estate Sign 2

Our company is called Corwin Hadley Realty. We are a real estate development company. We need a sign that we are going to hang outside of our projects that says: Another project brought to you by Corwin Hadley Realty... For Sale....(213) 555-0187. At the very bottom is needs to say CaBRE# 04637251" We want the Corwin Hadley Realty to be sophisticated, fresh, simple. We do not have a logo so maybe one can be incorporated into the sign. Sign will be about 30"x24"

Industry/Entity Type

Real Estate

```html
<!DOCTYPE html>
<html lang="en">
<head>
<meta charset="utf-8">
<title>Corwin Hadley Realty – For Sale Sign</title>
<link rel="stylesheet" href="https://fonts.googleapis.com/css2?family=Tinos:wght@400;700&display=swap">
<style>
  :root {
    --brand-red: #d71d26;
    --brand-red-dark: #a3172a;
    --earth-brown: #534332;
    --paper-white: #ffffff;
  }
  html, body {
    margin: 0;
    padding: 0;
    width: 1200px;
    height: 958px;
    overflow: hidden;
    background: var(--paper-white);
  }
  .sign {
    display: block;
    width: 1200px;
    height: 958px;
    font-family: "Tinos", "Times New Roman", serif;
  }
  .sign-text { fill: var(--paper-white); }
  .company-name { font-size: 166px; font-weight: 400; }
  .company-tag { font-size: 100px; font-weight: 400; }
  .monogram { font-size: 46px; font-weight: 400; fill: var(--brand-red); }
  .sale-label { font-size: 106px; font-weight: 400; }
  .phone { font-size: 112px; font-weight: 700; }
  .license { font-size: 32px; font-weight: 400; }
</style>
</head>
<body>
<svg class="sign" viewBox="0 0 1200 958" xmlns="http://www.w3.org/2000/svg" aria-label="Corwin Hadley Realty for sale sign">
  <defs>
    <radialGradient id="band-red" cx="50%" cy="50%" r="60%">
      <stop offset="0%" stop-color="#d71d26"/>
      <stop offset="100%" stop-color="#a3172a"/>
    </radialGradient>
    <linearGradient id="banner-red" x1="0" y1="0" x2="1" y2="0">
      <stop offset="0%" stop-color="#a3172a"/>
      <stop offset="45%" stop-color="#d71d26"/>
      <stop offset="100%" stop-color="#a3172a"/>
    </linearGradient>
  </defs>

  <!-- header band -->
  <rect class="header-band" x="0" y="0" width="1200" height="211" fill="url(#band-red)"/>
  <rect class="header-rule" x="0" y="211" width="1200" height="9" fill="var(--paper-white)"/>

  <!-- brand mark -->
  <circle class="brand-circle" cx="600" cy="107" r="62" fill="var(--paper-white)"/>
  <text class="monogram" x="600" y="123" text-anchor="middle">CHR</text>

  <!-- main panel -->
  <rect class="main-panel" x="0" y="220" width="1200" height="738" fill="var(--earth-brown)"/>

  <!-- company name -->
  <text class="sign-text company-name" x="113" y="344" textLength="975" lengthAdjust="spacing">CORWIN</text>
  <text class="sign-text company-name" x="113" y="474" textLength="975" lengthAdjust="spacing">HADLEY</text>
  <text class="sign-text company-tag" x="98" y="569" textLength="992" lengthAdjust="spacing">REALTY</text>

  <!-- for sale banner -->
  <polygon class="sale-banner" points="291,586 928,586 971,643 928,701 291,701" fill="url(#banner-red)"/>
  <text class="sign-text sale-label" x="320" y="674" textLength="580" lengthAdjust="spacing">FOR SALE</text>

  <!-- phone -->
  <text class="sign-text phone" x="262" y="793" textLength="718" lengthAdjust="spacing">(213) 555-0187</text>

  <!-- footer artwork area -->
  <rect class="footer-art" role="img" aria-label="Red house roofline illustration with chimneys" x="0" y="832" width="1200" height="126" fill="url(#banner-red)"/>

  <!-- license -->
  <text class="sign-text license" x="600" y="940" text-anchor="middle" letter-spacing="6">CaBre# 04637251</text>
</svg>
</body>
</html>
```